Weavers Of Vigour

Hi,

I am looking for a book cover for my first book Weavers of Vigour which will be published through printloom and zephyrn. It is a series of 42 interviews with pioneers and innovators in Complementary Therapy and Alternative Medicine. The book contains black and white portrait photographs of each person interviewed and is divided into three sections, body, mind and energy.

The title of the book is 'Weavers of Vigour' and the strapline is 'Complementary Therapy and Alternative Medicine through the eyes of its practitioners and innovators.'

I would like the book cover to be designed so it can fit into the requirements for print loom.

The feel of the cover needs to be beautifully striking, modern, Artistic and vibrant, embodying the theme of well being. I would like it to look clean and fresh.

I have enclosed further details on printloom dimensions for the book cover.

Please feel free to contact me if clarity is needed.

The text for the back cover is Back cover is -

Take a journey into your own body, mind and energy through the personal stories of some of holistic health and complementary medicine's most expansive and creative practitioners and teachers including:

Gerald Pinnock - Nutrition
Miriam Letcher - Hypnotherapy
Lantern Healer - Energy Work
Dana Quorrell - Yoga
Gwen Atherley - Pilates
Rob Dunmere - NLP
Tessa Brume - Voice Work
Joel Varnick - Sound Therapy

This book will give you an empowering 360 degree view of your own body’s natural capacity and intelligence to heal.

I have enclosed an image that I would like to use in the design

There have been changes to the brief.

Can you use the new brief as the guide for this project?

Thanks...

Industry/Entity Type

Health

Font styles to use
Serif

Colors
e34197
faed23
f78f20
eb1f27

```html
<!DOCTYPE html>
<html lang="en">
<head>
<meta charset="utf-8">
<title>Weavers of Vigour — Book Cover</title>
<link rel="stylesheet" href="https://fonts.googleapis.com/css2?family=Cinzel:wght@400;500&family=Alegreya:ital@1&display=swap">
<style>
  :root {
    --paper: #ffffff;
    --ink: #111111;
    --teal-deep: #0a9a8f;
    --teal-bright: #00cc8c;
    --title: #ffffff;
    --art-purple: #8a4fb0;
    --art-magenta: #e34197;
    --art-yellow: #e8d64a;
    --art-blue: #6fb3d9;
    --art-green: #4caf7a;
  }
  html, body {
    margin: 0;
    padding: 0;
    width: 800px;
    height: 1200px;
    overflow: hidden;
    background: var(--paper);
  }
  .cover {
    position: relative;
    width: 800px;
    height: 1200px;
    background: var(--paper);
    overflow: hidden;
  }
  .author-name {
    position: absolute;
    top: 12px;
    left: 0;
    width: 800px;
    margin: 0;
    text-align: center;
    font-family: "Cinzel", serif;
    font-weight: 500;
    font-size: 34px;
    letter-spacing: 0.5px;
    color: var(--ink);
  }
  .artwork {
    position: absolute;
  }
  .artwork--figure {
    left: 0;
    top: 0;
    width: 330px;
    height: 676px;
    background: linear-gradient(160deg, var(--art-purple) 0%, var(--art-blue) 35%, var(--art-yellow) 60%, var(--art-magenta) 85%, var(--art-green) 100%);
    border-radius: 0 140px 0 0;
  }
  .artwork--lotus-hand {
    left: 385px;
    top: 245px;
    width: 415px;
    height: 431px;
    background: linear-gradient(170deg, var(--art-purple) 0%, var(--art-magenta) 30%, var(--art-yellow) 60%, var(--art-blue) 85%, var(--art-green) 100%);
    border-radius: 200px 200px 0 120px;
  }
  .title-band {
    position: absolute;
    left: 0;
    top: 676px;
    width: 800px;
    height: 524px;
    background: radial-gradient(ellipse 70% 60% at 50% 50%, var(--teal-bright) 0%, var(--teal-deep) 100%);
    color: var(--title);
  }
  .title-line {
    position: absolute;
    left: 0;
    width: 800px;
    margin: 0;
    text-align: center;
    font-family: "Cinzel", serif;
    font-weight: 400;
    white-space: nowrap;
    line-height: 1;
  }
  .title-line--first { top: 8px; font-size: 134px; }
  .title-line--last { top: 232px; font-size: 150px; }
  .title-joiner {
    position: absolute;
    top: 172px;
    left: 50px;
    width: 700px;
    display: flex;
    align-items: center;
    gap: 30px;
  }
  .title-joiner .rule {
    flex: 1;
    height: 2px;
    background: var(--title);
  }
  .title-joiner .word {
    font-family: "Cinzel", serif;
    font-size: 64px;
    line-height: 1;
  }
  .strapline {
    position: absolute;
    top: 402px;
    left: 0;
    width: 800px;
    margin: 0;
    text-align: center;
    font-family: "Alegreya", serif;
    font-style: italic;
    font-size: 31px;
    line-height: 52px;
    color: var(--title);
  }
</style>
</head>
<body>
  <main class="cover">
    <div class="artwork artwork--figure" role="img" aria-label="Colourful patterned illustration of a woman in profile with flowing decorated hair"></div>
    <div class="artwork artwork--lotus-hand" role="img" aria-label="Colourful patterned illustration of an open hand holding a lotus flower"></div>
    <p class="author-name">Author Name</p>

    <section class="title-band">
      <h1 class="book-title">
        <span class="title-line title-line--first">WEAVERS</span>
        <span class="title-joiner"><span class="rule"></span><span class="word">OF</span><span class="rule"></span></span>
        <span class="title-line title-line--last">VIGOUR</span>
      </h1>
      <p class="strapline">Complementary Therapy and Alternative Medicine<br>through the eyes of its practitioners and innovators</p>
    </section>
  </main>
</body>
</html>
```